New design for a physiotherapy clinic specializing in laser therapy

BrightPath Physiotherapy is a unique clinic specializing in laser therapy. The clinic is now 7 years old and has a well established reputation for patient care.

We are the largest laser physiotherapy clinic in Mississauga, ON, Canada. We use state of the art laser therapy equipment. Our knowledge base of how to use Low Level Laser Therapy in conjunction with traditional physiotherapy is what sets us apart. Nobody wants to live with pain and everyone wants to get better as quickly as possible. Our treatment methodology helps our patients return to normal lives quickly.

We want a website that communicates expertise, trust and shows that we care for our patients. We also want people to understand that the treatments are painless and speed up healing naturally.
Updates

Please include a location tab in your submission.  This page should have a map of our location and our phone number.

I do not want any white coat and stethoscope people. We do not see hospitalized patients. We use Zorva-Kel NuvaQuill laser web site www.nuvaquilllaser.example please remove any images with other laser machines. I do not want "massage" therapy pictures as the main image. We treat post op total hip and knee replacements, rotator cuff injuries, osteoarthritic back pain patients, sprained ankles, degenerative disc disease problems as some of the more general injuries seen.

Industry/Entity Type

Clinic

Requirements
Must have
• We want to retain as much of the current content as possible. We will be looking at editing the content to make it shorter.

In addition to the current pages we want to add a blog page and link.

see our current site www.brightpathphysio.example
Nice to have
• Medical Images in the Whiplash and Auto Injuries should be re-drawn.

We want a clean, uncluttered look to the site.

Should not have
• Do not use illustrations of lasers shooting out or cutting. This is a "Cold" laser and does not cut. The laser procedure is gentle and soothing.

```html
<!DOCTYPE html>
<html lang="en">
<head>
<meta charset="utf-8">
<title>BrightPath Physiotherapy</title>
<link href="https://fonts.googleapis.com/css2?family=Arimo:wght@400;700&family=Open+Sans:ital@1&display=swap" rel="stylesheet">
<style>
:root{
  --green:#6ab42d;
  --green-text:#6aaf2a;
  --band-dark:#d6dcb8;
  --band-light:#e9ecd9;
  --panel:#d4dbb5;
  --ink:#222;
  --body:#333;
  --muted:#8a8a8a;
  --white:#fff;
  --rule:#c9cfad;
}
*{margin:0;padding:0;box-sizing:border-box}
html,body{width:999px;height:1200px;overflow:hidden}
body{position:relative;background:var(--band-light);font-family:"Arimo",Arial,sans-serif;color:var(--body)}
.abs{position:absolute}
.band-top{left:0;top:0;width:999px;height:87px;background:var(--band-dark)}
.band-hero{left:0;top:165px;width:999px;height:343px;background:var(--band-dark)}

.header{left:80px;top:0;width:833px;height:125px;background:var(--white)}
.brand{position:absolute;left:17px;top:38px;display:flex;align-items:center;gap:9px}
.brand-mark{width:20px;height:20px;border-radius:50%;background:var(--green)}
.brand-name{font-size:20px;font-weight:400;color:var(--ink)}
.contact{right:25px;top:31px;text-align:right;font-size:10.5px;line-height:14px;color:var(--ink)}
.contact b{font-weight:700}
.call{right:25px;top:94px;font-size:14px;font-weight:700;color:#444}
.call span{color:var(--green-text)}

.nav{left:80px;top:125px;width:833px;height:40px;background:var(--green)}
.nav a{color:var(--white);font-size:10px;font-weight:700;text-decoration:none;position:absolute;top:14px}

.hero{left:81px;top:166px;width:832px;height:340px;background:linear-gradient(90deg,#c9b5a6 0%,#b48a80 18%,#9a9a98 45%,#4a4c52 70%,#8d9096 100%)}
.hero-text{left:156px;top:238px;color:var(--white);font-size:29px;line-height:28px;font-weight:400}
.slider{left:80px;top:506px;width:833px;height:18px;background:var(--white)}
.dot{position:absolute;top:7px;width:9px;height:8px;background:#777}

.cards{left:80px;top:529px;width:833px;height:162px;background:var(--white)}
.card{position:absolute;top:0;height:162px;border-left:1px solid #e4e7d4;padding:23px 9px 0 10px}
.card:first-child{border-left:none}
.card h3{font-size:15px;font-weight:400;line-height:14px;color:var(--ink)}
.card h3 span{display:block;color:var(--green-text)}
.card p{margin-top:17px;width:182px;font-size:10px;line-height:14.1px;color:var(--ink)}
.more{font-size:10px;color:var(--green-text)}

.quick{left:80px;top:698px;width:211px;height:236px;background:var(--panel)}
.quick h2{position:absolute;left:13px;top:15px;font-size:15px;font-weight:400;color:var(--ink)}
.quick ul{list-style:none;position:absolute;left:12px;top:49px;width:174px}
.quick li{height:25px;border-bottom:1px solid #b9c096;font-size:10px;font-weight:700;color:var(--ink);padding:7px 0 0 12px;position:relative}
.quick li:last-child{border-bottom:none}
.quick li svg{position:absolute;left:0;top:9px}

.forms{left:80px;top:937px;width:211px;height:127px;background:var(--white)}
.forms h2{position:absolute;left:15px;top:12px;font-size:15px;font-weight:400;line-height:14px;color:var(--ink)}
.forms h2 span{display:block;color:var(--green-text)}
.forms p{position:absolute;left:15px;top:52px;font-size:10px;color:var(--ink)}
.select{position:absolute;left:13px;top:71px;width:160px;height:29px;border:1px solid #ccc;font-size:9.5px;color:#aaa;padding:9px 0 0 9px}
.select svg{position:absolute;right:8px;top:10px}
.dl{position:absolute;left:13px;top:110px;font-size:10px;color:var(--ink)}

.main{left:296px;top:698px;width:617px;height:366px;background:var(--white)}
.main h2{position:absolute;font-size:15px;font-weight:400;color:var(--ink)}
.main h2 span{color:var(--green-text)}
.photo{position:absolute;left:20px;top:39px;width:230px;height:117px;background:linear-gradient(90deg,#c99a70 0%,#e2d6c6 45%,#d9cdbd 70%,#b98d62 100%)}
.intro{position:absolute;left:266px;top:39px;width:343px;font-size:10px;line-height:16.6px;color:var(--muted)}
.intro2{position:absolute;left:20px;top:170px;width:560px;font-size:10px;line-height:14px;color:#666}
.viewall{position:absolute;left:486px;top:238px;font-size:10px;color:var(--ink)}
.avatar{position:absolute;left:26px;top:267px;width:86px;height:86px;border-radius:50%;background:linear-gradient(135deg,#9fb6c9,#4c6b8c)}
.quote{position:absolute;left:138px;top:284px;width:432px;font-family:"Open Sans",Arial,sans-serif;font-style:italic;font-size:12.5px;line-height:14px;color:var(--green-text)}

.rule{left:80px;top:1080px;width:833px;height:2px;background:var(--rule)}
.hours{left:92px;top:1102px;font-size:10px;line-height:11.7px;color:var(--ink)}
.hours b{font-weight:400;color:#444}
.copy{left:92px;top:1166px;font-size:10px;line-height:11.7px;color:var(--muted)}
.faddr{left:0;width:904px;top:1099px;text-align:right;font-size:10px;line-height:14px;color:var(--ink)}
.faddr b{font-weight:700}
.social{left:775px;top:1147px}
</style>
</head>
<body>
<div class="abs band-top"></div>
<div class="abs band-hero"></div>

<header class="abs header">
  <div class="brand">
    <span class="brand-mark"></span>
    <span class="brand-name">BrightPath Physiotherapy</span>
  </div>
  <div class="abs contact"><b>Our Address:</b><br>Harborview Centre, 4410 Alder Grove Parkway<br>Mississauga, ON L5X 2R4</div>
  <div class="abs call">CALL: <span>905-555-0148</span></div>
</header>

<nav class="abs nav">
  <a style="left:16px">HOME</a>
  <a style="left:68px">CLINIC HOURS</a>
  <a style="left:162px">PHYSIOTHERAPY</a>
  <a style="left:270px">LASER THERAPHY</a>
  <a style="left:383px">WHIPLASH &amp; AUTO INJURIES</a>
  <a style="left:548px">THERAPHY</a>
  <a style="left:617px">LOCATION</a>
  <a style="left:682px">BLOG</a>
  <a style="left:725px">CONTACT</a>
</nav>

<div class="abs hero" role="img" aria-label="Photo of a worried woman sitting beside a damaged car after an accident"></div>
<div class="abs hero-text">WE UNDERSTAND<br>how precious your<br>LIFE IS</div>
<div class="abs slider">
  <span class="dot" style="left:764px"></span><span class="dot" style="left:776px"></span><span class="dot" style="left:788px"></span><span class="dot" style="left:800px"></span><span class="dot" style="left:812px"></span>
</div>

<section class="abs cards">
  <div class="card" style="left:0;width:213px"><h3>PHYSIOTHERAPHY<span>CLINIC</span></h3><p>Praesent vestibulum molestie lacus. Abs an nonummy hendrerit mauris. Phasels porta. Fusce suscipit varius mi. Cumsd is natoque penatibus et magnis dis parr ient montes.<br><span class="more">READ MORE</span></p></div>
  <div class="card" style="left:213px;width:212px"><h3>LASER THERAPHY<span>CLINIC</span></h3><p>Praesent vestibulum molestie lacus. Abs an nonummy hendrerit mauris. Phasels porta. Fusce suscipit varius mi. Cumsd is natoque penatibus et magnis dis parr ient montes.<br><span class="more">READ MORE</span></p></div>
  <div class="card" style="left:425px;width:206px"><h3>MASSAGE THERAPHY<span>CLINIC</span></h3><p>Praesent vestibulum molestie lacus. Abs an nonummy hendrerit mauris. Phasels porta. Fusce suscipit varius mi. Cumsd is natoque penatibus et magnis dis parr ient montes.<br><span class="more">READ MORE</span></p></div>
  <div class="card" style="left:631px;width:202px"><h3>AUTO INJURY<span>CLINIC</span></h3><p>Praesent vestibulum molestie lacus. an nonummy hendrerit mauris. Phas porta. Fusce suscipit varius mi. Cum is natoque penatibus et magnis dis p ient montes.<br><span class="more">READ MORE</span></p></div>
</section>

<aside class="abs quick">
  <h2>QUICK LINKS</h2>
  <ul>
    <li><svg width="7" height="6"><path d="M0 3h5M3 1l2 2-2 2" stroke="#333" fill="none"/></svg>CLINIC HOURS</li>
    <li><svg width="7" height="6"><path d="M0 3h5M3 1l2 2-2 2" stroke="#333" fill="none"/></svg>VISITING OUR CLINIC - FAQ</li>
    <li><svg width="7" height="6"><path d="M0 3h5M3 1l2 2-2 2" stroke="#333" fill="none"/></svg>INSURANCE</li>
    <li><svg width="7" height="6"><path d="M0 3h5M3 1l2 2-2 2" stroke="#333" fill="none"/></svg>TESTIMONIALS</li>
    <li><svg width="7" height="6"><path d="M0 3h5M3 1l2 2-2 2" stroke="#333" fill="none"/></svg>BRIGHTPATH IN THE NEWS</li>
    <li><svg width="7" height="6"><path d="M0 3h5M3 1l2 2-2 2" stroke="#333" fill="none"/></svg>EMPLOYMENT</li>
  </ul>
</aside>

<aside class="abs forms">
  <h2>PATIENT DOWNLOAD<span>FORMS</span></h2>
  <p>Phasels porta. Fusce suscipit varius mi.</p>
  <div class="select">Select Service<svg width="10" height="8"><path d="M0 0h10L5 8z" fill="#555"/></svg></div>
  <div class="dl">Download Forms</div>
</aside>

<main class="abs main">
  <h2 style="left:20px;top:15px">WELCOME TO <span>BRIGHTPATH</span></h2>
  <div class="photo" role="img" aria-label="Photo of a bandaged ankle with crutches on a wooden floor"></div>
  <p class="intro">We are Mississauga's premier physiotherapy and low intensity laser therapy specialists. We integrate low intensity laser therapy (laser therapy or cold laser therapy) with physiotherapy to safely and effectively treat a wide variety of musculoskeletal injuries and inflammatory conditions (i.e. back pain, arthritis, knee injuries, shoulder injuries, tendonitis, bursitis, repetitive strains, auto &amp; sports injuries). This clinically proven program can achieve remarkable results for acute injury and chronic pain patients and is painless.</p>
  <p class="intro2">We Use a multi-faceted regime of clinically tested and proven protocols with one goal in mind: Get you better, faster.<br>Our results-focused team includes registered physiotherapists, registered massage therapists, certified kinesiologists and certified athletic therapists.</p>
  <h2 style="left:20px;top:236px">TESTIMONIALS</h2>
  <div class="viewall">View all testimonials</div>
  <div class="avatar" role="img" aria-label="Portrait photo of a patient giving a testimonial"></div>
  <p class="quote">Praesent vestibulum molestie lacus. Abs an nonummy hendrerit mauris. Phaselsporta. Fusce suscipit varius mi. Cumsd is natoque penatibus et magnis dis parr ient montes.</p>
</main>

<div class="abs rule"></div>
<footer>
  <div class="abs hours"><b>CLINIC HOURS</b><br>Monday, Wednesday &amp; Friday 9 am to 6 pm<br>Tuesday &amp; Thursday 11 am to 7 pm<br>Saturday 9 am to 12 pm</div>
  <div class="abs copy">Copyright 2013. All rights reserved.<br>Terms &amp; Conditions &nbsp;- &nbsp;Privacy &nbsp;- &nbsp;Disclaimer</div>
  <div class="abs faddr"><b>Our Address:</b><br>Harborview Centre, 4410 Alder Grove Parkway<br>Mississauga, ON L5X 2R4</div>
  <svg class="abs social" width="132" height="30" aria-label="Social links">
    <g fill="#e4e4e4" stroke="#888" stroke-width="1.5">
      <circle cx="16" cy="15" r="13"/><circle cx="48" cy="15" r="13"/><circle cx="80" cy="15" r="13"/><circle cx="112" cy="15" r="13"/>
    </g>
  </svg>
</footer>
</body>
</html>
```